Vitamin and Nutrition Ecommerce Site Needs a High End Website Design

We need a new and improved Homepage design for a leading Vitamin eCommerce business.
We supply our customers worldwide with leading brands of vitamin supplements and nutritional products at discounted prices.
The site design and layout must improve sales conversion and maximize the user experience staying on the site!

We will need to see;
A New Nutri Harbour stylized font (no logo)
High-End Modern Design
Easy Sales Conversion Experience
Excellent Layout, Fast Navigation
Quality Font style, Stylish Colour Palette Selection
Appropriate Spacing
Call To Action to Improve Sales Conversion
Web page should Look Clean and Minimalist

The design should improve sales, communicate easy to find products, facilitate fast ordering, have a modern and professional appearance centered toward a predominately female consumer.

Thank you for your interest in this project!

Current design can be found on this link;
www.nutriharbour.com.au/nutri/

Target Market(s)

80% Female 30-65 years

Industry/Entity Type

Business

Number of Pages Required

1 page

Colors

Designer to choose colors to be used in the design.

Requirements
Must have
• design must result improve sales conversion
• new Nutri Harbour font design
• search field
• attractive clean modern design
• stylish font and colour palette selection
Nice to have
• white background
Should not have
• cluttered or busy layout
• confusing navigation

```html
<!DOCTYPE html>
<html lang="en">
<head>
<meta charset="utf-8">
<title>Nutri Harbour – Vitamins &amp; Nutrition</title>
<link href="https://fonts.googleapis.com/css2?family=Raleway:wght@400;500;600;700&family=Open+Sans:ital,wght@0,400;0,600;0,700;1,700&display=swap" rel="stylesheet">
<style>
:root{
  --mint:#7ed6ad;
  --mint-dark:#5fc494;
  --brown:#5b4239;
  --brown-dark:#4a3530;
  --ink:#2f2f2f;
  --text:#555;
  --muted:#8a8a8a;
  --line:#dcdcdc;
  --grey-bg:#ebebeb;
  --orange:#f7a11a;
  --white:#fff;
}
*{box-sizing:border-box;margin:0;padding:0}
html,body{width:1200px;height:3435px;overflow:hidden}
body{font-family:"Open Sans",Arial,sans-serif;color:var(--text);background:var(--white);position:relative}
ul{list-style:none}
a{color:inherit;text-decoration:none}
.display{font-family:"Raleway",Arial,sans-serif}

/* Header */
.site-header{height:147px;position:relative}
.brand{position:absolute;left:100px;top:48px;font-family:"Raleway",sans-serif;font-weight:600;font-size:42px;color:var(--brown);letter-spacing:-.5px;display:flex;align-items:center;gap:12px}
.brand-dot{width:18px;height:18px;border-radius:50%;background:var(--mint)}
.account-links{position:absolute;left:688px;top:32px;display:flex;gap:28px;font-size:11.5px;font-weight:600;color:var(--brown-dark);text-transform:uppercase}
.account-links li{display:flex;align-items:center;gap:6px}
.search{position:absolute;left:676px;top:82px;width:252px;height:37px;border:1px solid #ccc;border-radius:19px;display:flex;align-items:center;padding:0 14px;font-size:11.5px;color:#999;justify-content:space-between}
.cart{position:absolute;left:955px;top:84px;display:flex;align-items:center;gap:8px;font-size:15px;color:var(--mint-dark)}
.cart-icon{width:32px;height:32px;border-radius:50%;background:var(--orange);display:flex;align-items:center;justify-content:center}

/* Nav */
.main-nav{height:53px;background:var(--mint)}
.main-nav ul{display:flex;justify-content:space-between;align-items:center;width:1000px;margin-left:100px;height:53px}
.main-nav li{font-family:"Raleway",sans-serif;font-weight:700;font-size:12.5px;color:var(--white);text-transform:uppercase;height:53px;line-height:53px}
.main-nav li.active{background:var(--brown);padding:0 20px}

/* Hero */
.hero{height:483px;position:relative;background:linear-gradient(90deg,#dcdcde 0%,#ececee 30%,#e3ddd8 55%,#efe9e4 75%,#f4f4f6 100%)}
.hero-title{position:absolute;left:120px;top:90px;width:330px;text-align:center;font-family:"Raleway",sans-serif;font-weight:700;font-size:44px;line-height:54px;color:var(--brown)}
.hero-arrow{position:absolute;top:408px;width:40px;height:40px;border-radius:50%;border:2px solid #999;display:flex;align-items:center;justify-content:center;background:rgba(255,255,255,.3)}
.hero-arrow.prev{left:30px}
.hero-arrow.next{right:30px}

/* Welcome */
.welcome{height:593px;position:relative;text-align:center}
.section-title{font-family:"Raleway",sans-serif;font-size:34px;color:var(--ink);font-weight:500}
.welcome .section-title{position:absolute;top:97px;left:0;right:0}
.welcome-intro{position:absolute;top:152px;left:180px;width:840px;font-size:12px;line-height:21px;color:#555}
.feature-list{position:absolute;top:281px;left:0;width:1200px}
.feature{position:absolute;width:280px;text-align:center}
.feature-icon{width:120px;height:120px;border-radius:50%;background:var(--mint);margin:0 auto;display:flex;align-items:center;justify-content:center}
.feature h3{font-family:"Open Sans",sans-serif;font-weight:400;font-size:19px;color:var(--ink);margin-top:34px}
.feature p{font-size:11.5px;line-height:19px;margin-top:12px;color:#666}

/* Why */
.why{height:556px;position:relative;background:linear-gradient(180deg,#e4e4e4,#efefef 50%,#e6e6e6)}
.why .section-title{position:absolute;top:50px;left:0;right:0;text-align:center;font-weight:600;color:var(--brown);font-size:35px}
.why-cards{position:absolute;top:137px;left:98px;display:flex;gap:14px}
.why-card{width:241px;height:296px;background:var(--white);box-shadow:0 2px 6px rgba(0,0,0,.18);text-align:center}
.why-card .photo{height:178px}
.why-card h3{font-weight:400;font-size:19px;color:var(--ink);margin-top:16px}
.why-card p{font-size:11px;line-height:17px;color:#666;padding:8px 22px 0}
.why-curve{position:absolute;left:0;bottom:0;width:1200px;height:60px}

/* Products */
.products{height:561px;position:relative;text-align:center}
.products .section-title{position:absolute;top:46px;left:0;right:0;font-weight:700;color:var(--brown);font-size:35px}
.product{position:absolute;top:138px;width:250px}
.product .photo{width:200px;height:195px;margin:0 auto}
.price{font-weight:700;font-style:italic;font-size:20px;color:var(--ink);margin-top:28px}
.product p{font-size:11.5px;line-height:17px;color:#555;margin-top:8px;padding:0 12px}
.btn-outline{display:inline-block;margin-top:16px;width:110px;height:26px;line-height:22px;border:2px solid #999;border-radius:13px;font-size:10px;font-weight:700;color:var(--ink);text-transform:uppercase}

/* Band */
.perks{height:133px;background:var(--mint);position:relative}
.perk{position:absolute;top:46px;display:flex;align-items:center;gap:14px;color:var(--white)}
.perk strong{display:block;font-family:"Raleway",sans-serif;font-size:16px;font-weight:600;text-transform:uppercase}
.perk span{font-size:11px}

/* Blog */
.blog{height:547px;position:relative}
.blog .section-title{position:absolute;top:78px;left:0;right:0;text-align:center;font-size:31px;text-transform:uppercase;color:#222}
.post{position:absolute;top:153px;width:312px}
.post .photo{height:190px;position:relative}
.date-badge{position:absolute;left:0;top:0;width:50px;height:52px;background:var(--mint);color:var(--white);text-align:center;font-weight:700;font-size:16px;line-height:20px;padding-top:5px}
.date-badge small{display:block;font-size:10px}
.post h3{font-size:17px;font-weight:700;color:#222;margin-top:22px}
.post p{font-size:11px;line-height:19px;color:#555;margin-top:10px}

/* Footer */
.site-footer{height:362px;background:var(--brown);color:var(--white);position:relative;font-size:11.5px}
.footer-brand{position:absolute;left:98px;top:70px;font-family:"Raleway",sans-serif;font-weight:600;font-size:30px}
.footer-contact{position:absolute;left:98px;top:136px}
.footer-contact li{display:flex;gap:12px;margin-bottom:16px;line-height:17px}
.footer-h{font-size:14px;font-weight:600;text-transform:uppercase}
.signup{position:absolute;left:378px;top:62px;width:270px}
.signup p{font-size:11px;line-height:18px;margin-top:12px;color:#e8dcd7}
.field{height:41px;border:1px solid #a28f88;margin-top:12px;padding:0 14px;line-height:39px;font-size:10px;color:#e8dcd7;position:relative}
.field .subscribe{position:absolute;right:-1px;top:-1px;height:41px;width:98px;background:var(--mint);color:var(--brown-dark);text-align:center;font-weight:700;text-transform:uppercase}
.footer-links{position:absolute;top:66px}
.footer-links ul{margin-top:14px}
.footer-links li{line-height:22.5px;font-size:11px}
.footer-links li::before{content:"›";margin-right:12px}
.footer-bottom{position:absolute;left:98px;right:98px;top:293px;border-top:1px solid #79615a;padding-top:22px;font-size:11px;display:flex;justify-content:space-between}
.payments{display:flex;gap:10px;margin-top:-6px}
.payments span{width:48px;height:28px;border-radius:3px;background:var(--white)}
</style>
</head>
<body>

<header class="site-header">
  <div class="brand"><span class="brand-dot"></span>Nutri Harbour</div>
  <ul class="account-links">
    <li><svg width="14" height="14" viewBox="0 0 14 14"><path d="M2 12V3h6M2 12h9V6M6 8l6-6" stroke="#4a3530" fill="none" stroke-width="1.5"/></svg>Register</li>
    <li><svg width="14" height="14" viewBox="0 0 14 14"><path d="M6 2h6v10H6M1 7h7M5 4l3 3-3 3" stroke="#4a3530" fill="none" stroke-width="1.5"/></svg>Login</li>
    <li><svg width="14" height="14" viewBox="0 0 14 14"><circle cx="7" cy="4" r="3" fill="#4a3530"/><path d="M1 14c0-4 3-6 6-6s6 2 6 6z" fill="#4a3530"/></svg>My Account</li>
    <li><svg width="16" height="14" viewBox="0 0 16 14"><path d="M1 1h3l2 8h8l1-6H5" stroke="#4a3530" fill="none" stroke-width="1.5"/><circle cx="7" cy="12" r="1.3" fill="#4a3530"/><circle cx="13" cy="12" r="1.3" fill="#4a3530"/></svg>Checkout</li>
  </ul>
  <div class="search">Search here
    <svg width="16" height="16" viewBox="0 0 16 16"><circle cx="7" cy="7" r="5" stroke="#777" stroke-width="1.6" fill="none"/><path d="M11 11l4 4" stroke="#777" stroke-width="1.8"/></svg>
  </div>
  <div class="cart"><span class="cart-icon"><svg width="18" height="16" viewBox="0 0 16 14"><path d="M1 1h3l2 8h8l1-6H5" stroke="#fff" fill="none" stroke-width="1.6"/><circle cx="7" cy="12" r="1.3" fill="#fff"/><circle cx="13" cy="12" r="1.3" fill="#fff"/></svg></span>Shopping Cart</div>
</header>

<nav class="main-nav">
  <ul>
    <li class="active">Home</li><li>Brand</li><li>Supplements</li><li>Sports Nutrition</li><li>Haircare</li><li>Chiropractic Pillows</li><li>Health Condition</li><li>Beauty &amp; Skincare</li><li>Contact</li>
  </ul>
</nav>

<section class="hero" role="img" aria-label="Photo of a woman taking a vitamin capsule with a glass of water beside jars of B vitamin supplements">
  <h1 class="hero-title">VITAMIN SUPPLEMENTS</h1>
  <span class="hero-arrow prev"><svg width="14" height="14" viewBox="0 0 14 14"><path d="M9 2L4 7l5 5" stroke="#777" stroke-width="2" fill="none"/></svg></span>
  <span class="hero-arrow next"><svg width="14" height="14" viewBox="0 0 14 14"><path d="M5 2l5 5-5 5" stroke="#777" stroke-width="2" fill="none"/></svg></span>
</section>

<section class="welcome">
  <h2 class="section-title">Welcome to Nutri Harbour!</h2>
  <p class="welcome-intro">With savings of up to 70% off Recommended Retail Prices we invite you to choose to shop with us at Nutri Harbour. Inside our online store you will find we are a leading Australian health retailer specialising in Professional, Fast and Reliable service for all your natural healthcare needs.</p>
  <div class="feature-list">
    <div class="feature" style="left:121px">
      <div class="feature-icon"><svg width="60" height="60" viewBox="0 0 60 60"><rect x="6" y="22" width="8" height="16" rx="2" fill="#fff"/><rect x="46" y="22" width="8" height="16" rx="2" fill="#fff"/><rect x="14" y="18" width="7" height="24" rx="2" fill="#fff"/><rect x="39" y="18" width="7" height="24" rx="2" fill="#fff"/><rect x="21" y="27" width="18" height="6" fill="#fff"/></svg></div>
      <h3>Sports Nutrition</h3>
      <p>Lorem ipsum dolor sit amet, consectetur adipiscing elit, sed do eiusmod tempor incididunt ut labore et dolore magna aliqua. Ut enim</p>
    </div>
    <div class="feature" style="left:458px">
      <div class="feature-icon"><svg width="60" height="60" viewBox="0 0 60 60"><path d="M30 50S8 36 8 22a11 11 0 0 1 22-4 11 11 0 0 1 22 4c0 14-22 28-22 28z" fill="none" stroke="#fff" stroke-width="4"/><path d="M14 30h10l4-7 5 12 4-5h9" fill="none" stroke="#fff" stroke-width="3"/></svg></div>
      <h3>Health Condition</h3>
      <p>Lorem ipsum dolor sit amet, consectetur adipiscing elit, sed do eiusmod tempor incididunt ut labore et dolore magna aliqua. Ut enim</p>
    </div>
    <div class="feature" style="left:794px">
      <div class="feature-icon"><svg width="60" height="60" viewBox="0 0 60 60"><rect x="12" y="8" width="14" height="8" fill="#fff"/><path d="M10 18h18v32H10z" fill="#fff"/><rect x="32" y="34" width="20" height="16" rx="3" fill="#fff"/><rect x="30" y="28" width="24" height="5" rx="2" fill="#fff"/></svg></div>
      <h3>Beauty &amp; Skincare</h3>
      <p>Lorem ipsum dolor sit amet, consectetur adipiscing elit, sed do eiusmod tempor incididunt ut labore et dolore magna aliqua. Ut enim</p>
    </div>
  </div>
</section>

<section class="why">
  <h2 class="section-title">WHY CHOOSE US</h2>
  <div class="why-cards">
    <article class="why-card"><div class="photo" role="img" aria-label="Portrait photo for skin care" style="background:linear-gradient(135deg,#c9a48c,#8d6450)"></div><h3>Skin Care</h3><p>Mauris vel lacus vitae felis vestibulum volutpat imperdiet ac nisl Cum sociis natoque sodales velit</p></article>
    <article class="why-card"><div class="photo" role="img" aria-label="Photo of glossy dark hair for hair care" style="background:linear-gradient(135deg,#3a3a3a,#111)"></div><h3>Hair Care</h3><p>Mauris vel lacus vitae felis vestibulum volutpat imperdiet ac nisl Cum sociis natoque sodales velit</p></article>
    <article class="why-card"><div class="photo" role="img" aria-label="Photo of supplement packs on special offer" style="background:linear-gradient(135deg,#f4f1ee,#9a6b4a)"></div><h3>Special Offers</h3><p>Mauris vel lacus vitae felis vestibulum volutpat imperdiet ac nisl Cum sociis natoque sodales velit</p></article>
    <article class="why-card"><div class="photo" role="img" aria-label="Photo of striped pillows on a sofa" style="background:linear-gradient(135deg,#b9b6b0,#6f6a64)"></div><h3>Chiropractic Pillows</h3><p>Mauris vel lacus vitae felis vestibulum volutpat imperdiet ac nisl Cum sociis natoque sodales velit</p></article>
  </div>
  <svg class="why-curve" viewBox="0 0 1200 60" preserveAspectRatio="none"><path d="M0 60V45Q600-10 1200 45V60z" fill="#fff"/><path d="M0 45Q600-10 1200 45" stroke="#7ed6ad" stroke-width="3" fill="none"/></svg>
</section>

<section class="products">
  <h2 class="section-title">OUR PRODUCTS</h2>
  <article class="product" style="left:79px"><div class="photo" role="img" aria-label="Amber supplement bottle" style="background:linear-gradient(180deg,#fff,#6b2e14 30%,#3b1808)"></div><div class="price">$25.99</div><p>Ut nisi erat fermentum vel congue id euismod in elit Fusce ultricies</p><span class="btn-outline">Add to Cart</span></article>
  <article class="product" style="left:342px"><div class="photo" role="img" aria-label="White supplement tub with capsules" style="background:linear-gradient(180deg,#fff,#ecece6 40%,#d9d6c8)"></div><div class="price">$25.99</div><p>Ut nisi erat fermentum vel congue id euismod in elit Fusce ultricies</p><span class="btn-outline">Add to Cart</span></article>
  <article class="product" style="left:601px"><div class="photo" role="img" aria-label="Black product jar with green label" style="background:linear-gradient(180deg,#fff,#1d1d1d 25%,#2f4a2c)"></div><div class="price">$25.99</div><p>Ut nisi erat fermentum vel congue id euismod in elit Fusce ultricies</p><span class="btn-outline">Add to Cart</span></article>
  <article class="product" style="left:869px"><div class="photo" role="img" aria-label="Three jars of B vitamin supplements" style="background:linear-gradient(180deg,#fff,#8a5a2a 30%,#3a2a22)"></div><div class="price">$25.99</div><p>Ut nisi erat fermentum vel congue id euismod in elit Fusce ultricies</p><span class="btn-outline">Add to Cart</span></article>
</section>

<section class="perks">
  <div class="perk" style="left:110px"><svg width="46" height="32" viewBox="0 0 46 32"><rect x="0" y="4" width="28" height="18" fill="#fff"/><path d="M30 10h9l6 7v5H30z" fill="#fff"/><circle cx="9" cy="26" r="5" fill="#fff"/><circle cx="36" cy="26" r="5" fill="#fff"/></svg><div><strong>Free Shipping</strong><span>for all orders over $99</span></div></div>
  <div class="perk" style="left:350px"><svg width="34" height="34" viewBox="0 0 34 34"><circle cx="17" cy="17" r="17" fill="#fff"/><path d="M9 17l6 6 11-12" stroke="#7ed6ad" stroke-width="3.5" fill="none"/></svg><div><strong>Official Stockist</strong><span>of more than 100 brands</span></div></div>
  <div class="perk" style="left:607px"><svg width="34" height="34" viewBox="0 0 34 34"><circle cx="17" cy="17" r="17" fill="#fff"/><path d="M9 17l6 6 11-12" stroke="#7ed6ad" stroke-width="3.5" fill="none"/></svg><div><strong>2 Free Samples</strong><span>on all orders over $99</span></div></div>
  <div class="perk" style="left:843px"><svg width="34" height="34" viewBox="0 0 34 34"><circle cx="17" cy="17" r="17" fill="#fff"/><path d="M9 17l6 6 11-12" stroke="#7ed6ad" stroke-width="3.5" fill="none"/></svg><div><strong>Verified Store</strong><span>rating of 4.9/5</span></div></div>
</section>

<section class="blog">
  <h2 class="section-title">Latest Blog</h2>
  <article class="post" style="left:98px"><div class="photo" role="img" aria-label="Photo of a pharmacist holding an apple" style="background:linear-gradient(135deg,#dfe9ee,#9fb8c4)"><span class="date-badge">02<small>JUN</small></span></div><h3>Lorem ipsum dolor sit amet,</h3><p>Lorem ipsum dolor sit amet, consectetur adipiscing elit. Sed blandit massa vel mauris sollicitudin dignissim. Lorem ipsum dolor sit amet, consectetur</p></article>
  <article class="post" style="left:444px"><div class="photo" role="img" aria-label="Photo of a woman drinking a smoothie with fresh juices" style="background:linear-gradient(135deg,#7a5a48,#c0503a)"><span class="date-badge">02<small>JUN</small></span></div><h3>Lorem ipsum dolor sit amet,</h3><p>Lorem ipsum dolor sit amet, consectetur adipiscing elit. Sed blandit massa vel mauris sollicitudin dignissim. Lorem ipsum dolor sit amet, consectetur</p></article>
  <article class="post" style="left:790px"><div class="photo" role="img" aria-label="Photo of a woman shopping in a pharmacy aisle" style="background:linear-gradient(135deg,#cfe0d6,#7fb39a)"><span class="date-badge">02<small>JUN</small></span></div><h3>Lorem ipsum dolor sit amet,</h3><p>Lorem ipsum dolor sit amet, consectetur adipiscing elit. Sed blandit massa vel mauris sollicitudin dignissim. Lorem ipsum dolor sit amet, consectetur</p></article>
</section>

<footer class="site-footer">
  <div class="footer-brand">Nutri Harbour</div>
  <ul class="footer-contact">
    <li><svg width="12" height="16" viewBox="0 0 12 16"><path d="M6 16S0 9 0 6a6 6 0 0 1 12 0c0 3-6 10-6 10z" fill="#fff"/><circle cx="6" cy="6" r="2.2" fill="#5b4239"/></svg><span>68 Harbour Lane<br>Wellington</span></li>
    <li><svg width="14" height="14" viewBox="0 0 14 14"><path d="M3 0l3 3-2 2c1 2 3 4 5 5l2-2 3 3-2 3C6 14 0 8 0 3z" fill="#fff"/></svg><span>Phone: 0800 55 12 40</span></li>
    <li><svg width="14" height="12" viewBox="0 0 14 12"><rect width="14" height="12" rx="1" fill="#fff"/><path d="M0 1l7 6 7-6" stroke="#5b4239" stroke-width="1.4" fill="none"/></svg><span>hello@nutriharbour.com.au</span></li>
  </ul>
  <div class="signup">
    <div class="footer-h">Sign up to receive email</div>
    <p>Excepteur sint occaecat cupidatat non proident, sunt in culpa qui</p>
    <div class="field">Enter Name</div>
    <div class="field">Enter Email<span class="subscribe">Subscribe</span></div>
  </div>
  <div class="footer-links" style="left:772px">
    <div class="footer-h">Quick Links</div>
    <ul><li>Home</li><li>About</li><li>Contact Us</li><li>Privacy Policy</li><li>Terms &amp; Conditions</li><li>Blog</li></ul>
  </div>
  <div class="footer-links" style="left:1021px">
    <div class="footer-h">Account</div>
    <ul><li>Payment</li><li>Save cards</li><li>Shipping</li><li>Return</li><li>FAQ</li><li>Check out</li></ul>
  </div>
  <div class="footer-bottom">
    <span>© 2017 Nutri Harbour. All Rights Reserved.</span>
    <div class="payments" aria-label="Accepted payment cards"><span></span><span></span><span></span></div>
  </div>
</footer>

</body>
</html>
```